Website design for an existing website that is currently live.

The website is vrolpworkshops.com and this will be the easiest design you will ever do because he LOVES his existing website and I convinced him to "modernize it" a bit. That means that it's not a from scratch design. All I need is to take the existing design and modify it to be more up to date with current design trends. To make it easier, I also have the original psd file from 2016 that I included in the project. For deails, it's really easy. Go to vrolpworkshops.com and use the same navigation, links, highlighted areas etc.. it's ok to move them around etc but it must contain all the current links because it's going to replace a live site. I will need a home page design and a simplified inner page design that I can use to plug in the content.

```html
<!DOCTYPE html>
<html lang="en">
<head>
<meta charset="utf-8">
<title>VROLPWORKSHOPS – Online Chiropractic CE</title>
<link href="https://fonts.googleapis.com/css2?family=Lato:wght@400;700&family=Montserrat:wght@400;500;600;700;800&display=swap" rel="stylesheet">
<style>
:root{
  --blue:#1a7fe0;
  --blue-dark:#0e55b5;
  --navy:#15439a;
  --ink:#1d1d1f;
  --text:#3b3b3b;
  --grey-bg:#f1f3f7;
  --white:#ffffff;
}
*{box-sizing:border-box;margin:0;padding:0}
html,body{width:1200px;height:2772px;overflow:hidden}
body{position:relative;font-family:'Lato',sans-serif;color:var(--text);background:var(--white)}
.abs{position:absolute}
a{color:inherit;text-decoration:none}

/* header */
.header{left:0;top:0;width:1200px;height:100px;background:var(--white);z-index:3}
.utility-bar{left:745px;top:0;width:455px;height:38px;background:var(--blue);clip-path:polygon(0 0,100% 0,100% 100%,25px 100%)}
.utility-bar a{position:absolute;top:12px;font:600 11px 'Montserrat',sans-serif;color:var(--white)}
.login-pill{position:absolute;left:278px;top:5px;width:76px;height:28px;border-radius:14px;background:var(--navy);color:#fff;font:600 11px 'Montserrat',sans-serif;text-align:center;line-height:28px}
.brand{left:118px;top:10px;display:flex;align-items:center;gap:8px}
.brand-mark{width:46px;height:46px;border-radius:50%;background:var(--blue)}
.brand-name{font:700 21px 'Montserrat',sans-serif;color:var(--ink);line-height:1}
.brand-sub{font:400 13px 'Montserrat',sans-serif;color:var(--text);margin-top:3px}
.main-nav{left:0;top:60px;width:1200px;height:40px;font:500 12.5px 'Montserrat',sans-serif;color:var(--ink)}
.main-nav a{position:absolute;top:0;white-space:nowrap}
.main-nav .active{font-weight:700}
.nav-underline{left:361px;top:96px;width:81px;height:4px;background:var(--blue)}

/* hero */
.hero{left:0;top:100px;width:1200px;height:580px;background:linear-gradient(110deg,#4a3e33 0%,#7b6a58 40%,#b69a7f 65%,#d4c6b6 100%)}
.hero-kicker{left:0;top:266px;width:1170px;text-align:center;font:400 28px 'Lato',sans-serif;color:#fff}
.hero-title{left:0;top:298px;width:1170px;text-align:center;font:800 50px 'Montserrat',sans-serif;color:#fff}
.search-bar{left:184px;top:364px;width:823px;height:100px;background:rgba(26,127,224,.92);border-radius:36px 0 36px 0}
.select{position:absolute;top:30px;height:40px;border:1px solid rgba(255,255,255,.75);color:#fff;font:600 11.5px 'Montserrat',sans-serif;padding:12px 10px;white-space:nowrap}
.select svg{position:absolute;right:9px;top:15px}
.search-btn{position:absolute;left:671px;top:30px;width:128px;height:40px;background:var(--navy);color:#fff;font:700 14px 'Montserrat',sans-serif;text-align:center;line-height:40px}

/* free class */
.frame-accent{left:110px;top:729px;width:234px;height:200px;background:var(--blue)}
.photo-doctor{left:125px;top:742px;width:446px;height:317px;border-radius:0 48px 0 48px;background:linear-gradient(120deg,#e9d8c8,#f4efe9 60%,#e6d3b0)}
.dots{left:485px;top:972px;width:110px;height:110px;background-image:radial-gradient(#b9bdc6 1.3px,transparent 1.6px);background-size:12px 12px}
.section-title{font:400 28px 'Montserrat',sans-serif;color:var(--ink);line-height:1.25}
.section-title b{font-weight:800}
.rule{width:74px;height:3px;background:var(--blue-dark)}
.free-copy{left:644px;top:852px;width:430px;font-size:16px;line-height:27px;color:var(--text)}
.free-btn{left:644px;top:1014px;width:415px;height:45px;background:var(--blue);color:#fff;font:700 15px 'Lato',sans-serif;text-align:center;line-height:45px}
.free-btn u{text-decoration:underline}

/* info section */
.grey-band{left:0;top:1125px;width:1200px;height:895px;background:var(--grey-bg)}
.info-heading{left:111px;top:1248px;width:560px;font:700 20px 'Montserrat',sans-serif;color:var(--ink);line-height:35px}
.feature-icon{width:60px;height:60px;border-radius:50%;background:var(--blue-dark)}
.feature-title{font:700 17.5px 'Montserrat',sans-serif;color:var(--blue);line-height:19px}
.feature-copy{font-size:13px;line-height:18.5px;color:var(--text)}
.nav-panel{left:698px;top:1233px;width:419px;height:694px;background:var(--white);border-radius:56px 0 0 0;overflow:hidden}
.nav-panel h3{position:absolute;left:52px;top:45px;font:400 20px 'Montserrat',sans-serif;color:var(--blue-dark)}
.nav-panel h3 b{font-weight:800}
.step{position:absolute;left:52px;display:flex;gap:14px;align-items:flex-start}
.step-ring{width:76px;height:76px;border:2px solid var(--blue-dark);border-radius:50%;display:flex;align-items:center;justify-content:center;flex:none}
.step p{font-size:14px;line-height:19px;color:var(--ink);margin-top:12px}
.step p b{font-weight:700}
.note{position:absolute;left:58px;top:358px;width:300px;font-size:10.5px;line-height:18px;color:var(--ink)}
.photo-student{position:absolute;left:0;top:420px;width:419px;height:274px;background:linear-gradient(100deg,#dbe3ea,#eef0f2 50%,#cfc8c0)}

/* cta */
.cta{left:0;top:2016px;width:1200px;height:391px;background:linear-gradient(100deg,#3a4452,#5b6877 45%,#7d8691)}
.cta h2{position:absolute;left:0;top:110px;width:1222px;text-align:center;font:400 32px 'Montserrat',sans-serif;color:#fff}
.cta h2 b{font-weight:800}
.cta p{position:absolute;left:270px;top:170px;width:700px;text-align:center;font:400 15px 'Montserrat',sans-serif;line-height:19px;color:#fff}
.cta-btn{position:absolute;left:515px;top:227px;width:184px;height:47px;border:2px solid #fff;color:#fff;font:700 17px 'Montserrat',sans-serif;text-align:center;line-height:43px}

/* footer */
.footer{left:0;top:2407px;width:1200px;height:365px;background:var(--blue)}
.footer-heading{font:500 17px 'Montserrat',sans-serif;color:var(--white)}
.f-rule{width:36px;height:2px;background:#fff;margin-top:6px}
.footer-links{display:grid;grid-template-columns:172px 120px;row-gap:15px;font:400 12.5px 'Montserrat',sans-serif;color:#fff}
.social{display:flex;gap:8px}
.social span{width:27px;height:27px;border-radius:50%;border:2.5px solid #fff}
.login-panel{left:797px;top:2407px;width:242px;height:270px;background:var(--navy);clip-path:polygon(0 0,100% 0,100% 100%,60% 94%,30% 96%,0 100%)}
.field{position:absolute;left:28px;width:190px;height:27px;border-radius:14px;background:#fff;font:400 9px 'Montserrat',sans-serif;color:#777;padding:8px 12px}
.login-btn{position:absolute;left:28px;top:177px;width:190px;height:27px;border-radius:14px;background:var(--blue);color:#fff;font:700 11px 'Montserrat',sans-serif;text-align:center;line-height:27px}
.copyright{left:0;top:2707px;width:1200px;border-top:1px solid rgba(255,255,255,.35);padding-top:30px;text-align:center;font:400 10.5px 'Montserrat',sans-serif;color:#dfe9f8}
</style>
</head>
<body>

<header class="header abs">
  <div class="utility-bar abs">
    <a style="left:49px">TESTIMONIALS</a>
    <a style="left:167px">CONTACT US</a>
    <span class="login-pill">LOGIN</span>
  </div>
  <div class="brand abs">
    <span class="brand-mark"></span>
    <div><div class="brand-name">VROLPWORKSHOPS</div><div class="brand-sub">Online Chiropractic CE</div></div>
  </div>
  <nav class="main-nav abs">
    <a class="active" style="left:367px">COURSES</a>
    <a style="left:462px">CERTIFICATION PROGRAMS</a>
    <a style="left:672px">MEET THE FACULTY</a>
    <a style="left:834px">FAQS</a>
    <a style="left:904px">STATE APPROVALS</a>
  </nav>
  <div class="nav-underline abs"></div>
  <svg class="abs" style="left:1046px;top:56px" width="34" height="30" viewBox="0 0 34 30" fill="none" stroke="#1a7fe0" stroke-width="2.5"><path d="M1 2h6l4 18h18l4-13H9"/><circle cx="13" cy="26" r="2.5"/><circle cx="27" cy="26" r="2.5"/></svg>
</header>

<section class="hero abs" role="img" aria-label="Photo of a smiling student working on a laptop in a library"></section>
<svg class="abs" style="left:0;top:600px" width="1200" height="82" viewBox="0 0 1200 82"><path d="M0 82V75C250 40 420 20 600 40 800 60 1000 62 1200 0V82Z" fill="#fff"/><path d="M65 58C300 20 420 18 620 40 820 62 1000 60 1120 42" stroke="#1a7fe0" stroke-width="6" fill="none"/></svg>
<div class="hero-kicker abs">Online Chiropractic CE Available</div>
<h1 class="hero-title abs">INCREASE YOUR VALUE</h1>
<div class="search-bar abs">
  <div class="select" style="left:26px;width:155px">Course Format<svg width="12" height="8" viewBox="0 0 12 8"><path d="M1 1l5 5 5-5" stroke="#fff" stroke-width="2" fill="none"/></svg></div>
  <div class="select" style="left:189px;width:155px">Topic<svg width="12" height="8" viewBox="0 0 12 8"><path d="M1 1l5 5 5-5" stroke="#fff" stroke-width="2" fill="none"/></svg></div>
  <div class="select" style="left:350px;width:155px">CE Hours<svg width="12" height="8" viewBox="0 0 12 8"><path d="M1 1l5 5 5-5" stroke="#fff" stroke-width="2" fill="none"/></svg></div>
  <div class="select" style="left:510px;width:155px;font-size:10.5px;padding-right:24px">Certificate Programs<svg width="12" height="8" viewBox="0 0 12 8"><path d="M1 1l5 5 5-5" stroke="#fff" stroke-width="2" fill="none"/></svg></div>
  <div class="search-btn">SEARCH</div>
</div>

<div class="frame-accent abs"></div>
<div class="photo-doctor abs" role="img" aria-label="Photo of a chiropractor examining a spine model"></div>
<div class="dots abs"></div>
<h2 class="section-title abs" style="left:644px;top:752px">TRY OUR FREE ONLINE<br><b>CHIROPRACTIC CLASS</b></h2>
<div class="rule abs" style="left:646px;top:828px"></div>
<p class="free-copy abs">If you have never taken an online course, we suggest starting with our free 1 hour program in Coding &amp; Documentation. By taking this course you will obtain a true sample of just how easy it is to take one of our courses and receive CE credit (approved in most states).</p>
<a class="free-btn abs">Please click <u>HERE</u> to try Online Chiropractic CE for free!</a>

<div class="grey-band abs"></div>
<svg class="abs" style="left:0;top:1110px" width="1200" height="70" viewBox="0 0 1200 70"><path d="M0 70V68C200 25 350 10 600 30 850 50 1050 40 1200 0V0H0Z" fill="#fff"/><path d="M130 32C300 10 420 8 620 30 820 52 980 50 1060 40" stroke="#1a7fe0" stroke-width="5" fill="none"/></svg>

<h2 class="info-heading abs">GET CHIROPRACTIC CEU CREDIT HOURS ONLINE THROUGH RECORDED WEBINARS, LIVE WEBINARS OR IN PERSON WITH OUR SEMINARS</h2>
<div class="rule abs" style="left:112px;top:1355px"></div>

<div class="feature-icon abs" style="left:102px;top:1398px"></div>
<svg class="abs" style="left:117px;top:1411px" width="30" height="34" viewBox="0 0 30 34" fill="none" stroke="#fff" stroke-width="1.6"><rect x="3" y="4" width="22" height="28" rx="2"/><rect x="9" y="1" width="10" height="5" rx="1"/><path d="M8 13h12M8 18h12M8 23h8"/><circle cx="24" cy="28" r="4"/></svg>
<div class="feature-title abs" style="left:178px;top:1406px">What could be better than having a choice?</div>
<p class="feature-copy abs" style="left:178px;top:1438px;width:460px">At VROLPWORKSHOPS you have a choice. We have online chiropractic CE courses available 24/7, live webinars, and onsite seminars! Imagine, now you can take CE classes at home, at the office, or on the go. Our online CE classes are compatible with your smart device, Mac, and PC! Online Chiropractic Continuing Education now accounts for more than half of the CE hours obtained by chiropractors and is growing. More than 40 states currently accept some or all of the required continuing education hours to be obtained online. Online chiropractic continuing education provides high quality interactive courses for less cost than an onsite seminar.</p>

<div class="feature-icon abs" style="left:94px;top:1632px"></div>
<svg class="abs" style="left:108px;top:1646px" width="32" height="32" viewBox="0 0 32 32" fill="none" stroke="#fff" stroke-width="1.6"><circle cx="16" cy="17" r="12" stroke-dasharray="3 2"/><path d="M16 9v8l5 4"/><path d="M24 4l4 4"/></svg>
<div class="feature-title abs" style="left:177px;top:1644px">There is no travel or lost time from<br>your family or practice.</div>
<p class="feature-copy abs" style="left:177px;top:1691px;width:475px">Chiropractic online continuing education courses have come a long way. Gone are the days of reading pages of material and waiting to answer a question before moving to the next page. Our programs use engaging slides, video, and handouts. You simply sit back and enjoy the presentation. You may even start one of our online seminars, log out and log back in to complete it at YOUR convenience! When the presentation is completed you may print your certificate of completion directly from the website, and, you always have access to your transcripts. We will be deploying online courses in all available states and will launch 10-15 additional hours monthly, ongoing.<br><br>We are always adding new faculty. Our new instructors will be the best of the best from the chiropractic profession! Please see our faculty page.<br>We look forward to serving YOU!</p>

<aside class="nav-panel abs">
  <h3><b>SITE NAVIGATION</b> INSTRUCTION</h3>
  <div class="step" style="top:97px">
    <span class="step-ring"><svg width="34" height="40" viewBox="0 0 34 40" fill="none" stroke="#0e55b5" stroke-width="1.8"><rect x="3" y="2" width="28" height="36" rx="2"/><path d="M9 10h5v5H9zM9 20h5v5H9zM18 12h8M18 22h8M9 31h17"/></svg></span>
    <p><b>Click on Course Format:</b><br>Choose Online, Webinar or Seminar</p>
  </div>
  <div class="step" style="top:187px">
    <span class="step-ring"><svg width="34" height="40" viewBox="0 0 34 40" fill="none" stroke="#0e55b5" stroke-width="1.8"><path d="M13 22V8a3 3 0 016 0v11l8 2c2 .5 3 2 3 4l-1 8c-.5 3-2 5-5 5H16c-2 0-3-1-4-2l-7-8c-1-1.5 0-4 2.5-3.5L13 26"/><path d="M8 8a8 8 0 0116 0"/></svg></span>
    <p><b>Click on Topic:</b><br>Choose a Topic from Bullet Proof<br>Documentation to Whiplash</p>
  </div>
  <div class="step" style="top:283px">
    <span class="step-ring"><svg width="40" height="40" viewBox="0 0 40 40" fill="none" stroke="#0e55b5" stroke-width="1.8"><circle cx="16" cy="16" r="12"/><circle cx="16" cy="16" r="8"/><path d="M25 25l12 12"/></svg></span>
    <p><b>Click on Search:</b><br>You will then see a list of courses to<br>choose from.</p>
  </div>
  <p class="note">*Please confirm that the course is approved in YOUR state. Each course has a list of state approvals. Alternately, you can click on State Approvals.</p>
  <div class="photo-student" role="img" aria-label="Photo of a smiling woman studying at a laptop"></div>
</aside>

<section class="cta abs" role="img" aria-label="Background photo of hands typing on a laptop keyboard">
  <h2>OFFERING <b>CERTIFICATION PROGRAMS</b></h2>
  <p>Lorem ipsum dolor sit amet, consectetur adipiscing elit, sed do eiusmod tempor incididunt ut labore et dolore magna aliqua. Ut enim ad minim veniam, quis nostrud exercitation ulla</p>
  <a class="cta-btn">GET STARTED</a>
</section>

<footer class="footer abs"></footer>
<div class="abs" style="left:143px;top:2472px">
  <h4 class="footer-heading">Contact VROLP Workshops</h4><div class="f-rule"></div>
  <div style="margin-top:17px;font:400 12.5px 'Montserrat',sans-serif;color:#fff">Chiropractic CE Registration &amp; Questions:</div>
  <div style="margin-top:8px;display:flex;align-items:center;gap:7px;font:600 16px 'Montserrat',sans-serif;color:#fff">
    <svg width="24" height="24" viewBox="0 0 24 24" fill="none" stroke="#fff" stroke-width="1.8"><circle cx="12" cy="12" r="11"/><path d="M8 6l2 3-1.5 1.5c1 2 2.5 3.5 4.5 4.5L14.5 13.5l3 2-1 2.5c-5 0-10-5-10-10z"/></svg>(555) 014-2290</div>
  <div class="social" style="margin-top:22px;margin-left:4px"><span></span><span></span><span></span><span></span></div>
</div>
<div class="abs" style="left:490px;top:2466px">
  <h4 class="footer-heading">Online Chiropractic CE</h4><div class="f-rule"></div>
  <div class="footer-links" style="margin-top:12px;margin-left:6px">
    <a>Home</a><a>Testimonials</a><a>Courses</a><a>State Approvals</a><a>Certification Programs</a><a>Contact Us</a><a>Meet the Faculty</a><a>FAQs</a>
  </div>
</div>
<div class="login-panel abs">
  <h4 class="footer-heading" style="position:absolute;left:29px;top:57px">Student Login</h4>
  <div class="f-rule" style="position:absolute;left:29px;top:82px;width:30px"></div>
  <div class="field" style="top:100px">Email</div>
  <div class="field" style="top:139px">•••••••</div>
  <div class="login-btn">LOGIN</div>
  <div style="position:absolute;left:0;top:218px;width:250px;text-align:center;font:600 9px 'Montserrat',sans-serif;color:#fff;text-decoration:underline">Forgot Username or Password?</div>
</div>
<div class="copyright abs">© 2021 Company Name | All Rights Reserved</div>

</body>
</html>
```